Real Estate Agent needs a Postcard Design

I need a postcard design for a marketing campaign in a specific area where I just sold 3 listings and they are all the highest sales in that community (Evergreen in San Jose, CA). The design should include my information, my picture, logo and the information on the 3 properties that I just sold.
4179 Pembrook Street in San Jose CA, sold for $810,000
4163 Pembrook Street in San Jose CA, sold for $816,000
4127 Pembrook Street in San Jose CA sold for $820,488

I am attaching pictures of the properties, my picture, and the company logo. Also I am attaching a sample of another postcard we used for another campaign. I need the front and back images of the postcards sent separately in jpeg format saved with a 300 DPI for best print resolution and also I would like to have a file that I can modify in case I want to add or delete any of the information.
Thank you and please contact me with questions.

```html
<!DOCTYPE html>
<html lang="en">
<head>
<meta charset="utf-8">
<title>Evergreen Postcard – Front and Back</title>
<link href="https://fonts.googleapis.com/css2?family=PT+Sans+Narrow:wght@400;700&display=swap" rel="stylesheet">
<style>
  :root {
    --page-bg: #e9e6e1;
    --forest: #0f4631;
    --forest-ring: #1f6a46;
    --leaf: #3f9463;
    --tag-green: #2b7a52;
    --tag-dark: #1e5c3d;
    --muted-green: #5f9277;
    --white: #ffffff;
    --brand-red: #b51f24;
    --ink: #1f1f1f;
    --rule: #c9c9c9;
    --stamp: #c8c8c8;
  }
  * { margin: 0; padding: 0; box-sizing: border-box; }
  html, body {
    width: 1200px; height: 750px; overflow: hidden;
    background: var(--page-bg);
    font-family: "PT Sans Narrow", "Arial Narrow", sans-serif;
  }
  .stage { position: relative; width: 1200px; height: 750px; }

  /* Front */
  .card-front {
    position: absolute; left: 44px; top: 46px;
    width: 538px; height: 348px;
    box-shadow: 0 2px 8px rgba(0,0,0,.25);
  }
  .card-front svg { display: block; }
  .headline { fill: var(--white); font-weight: 700; font-size: 19px; }
  .headline-area { fill: var(--leaf); font-weight: 700; font-size: 25px; }
  .subline { fill: var(--white); font-size: 14px; }
  .back-hint { fill: var(--muted-green); font-size: 9px; font-style: italic; }
  .tag-street { fill: var(--white); font-size: 9px; font-weight: 700; }
  .tag-number { fill: var(--white); font-size: 13px; }
  .tag-sold { fill: var(--white); font-size: 9px; font-style: italic; }
  .tag-price { fill: var(--white); font-size: 14px; font-weight: 700; }

  /* Back */
  .card-back {
    position: absolute; left: 606px; top: 346px;
    width: 544px; height: 352px;
    background: var(--white);
    box-shadow: 0 2px 8px rgba(0,0,0,.25);
  }
  .brand {
    position: absolute; left: 50px; top: 44px;
    display: flex; align-items: center; gap: 6px;
    color: var(--brand-red); font-weight: 700; font-size: 22px;
  }
  .brand-mark { width: 12px; height: 12px; background: var(--brand-red); }
  .stamp-box {
    position: absolute; left: 476px; top: 37px;
    width: 40px; height: 44px; background: var(--stamp);
  }
  .address-lines { position: absolute; left: 389px; top: 148px; width: 127px; }
  .address-lines span { display: block; height: 22px; border-bottom: 1px solid var(--rule); }
  .agent-photo {
    position: absolute; left: 0; top: 105px; width: 126px; height: 199px;
    background: linear-gradient(180deg, #b59c78 0%, #8d7658 45%, #1d2230 100%);
  }
  .agent-panel {
    position: absolute; left: 126px; top: 105px; width: 235px; height: 199px;
    background: var(--brand-red); color: var(--white);
    padding: 22px 14px 0 22px;
  }
  .panel-title { font-weight: 700; font-size: 13.5px; margin-bottom: 9px; }
  .panel-copy { font-size: 12px; line-height: 14px; }
  .agent-name {
    position: absolute; left: 13px; top: 160px;
    font-weight: 700; font-size: 15px;
  }
  .agent-licence { position: absolute; left: 15px; top: 179px; font-size: 9.5px; }
  .agent-phone {
    position: absolute; left: 132px; top: 161px;
    display: flex; align-items: center; gap: 4px; font-size: 13.5px;
  }
  .agent-phone svg { width: 10px; height: 10px; }
  .agent-email { position: absolute; left: 132px; top: 179px; font-size: 9.5px; }
</style>
</head>
<body>
<main class="stage">

  <section class="card-front" aria-label="Postcard front">
    <svg width="538" height="348" viewBox="0 0 538 348" xmlns="http://www.w3.org/2000/svg">
      <defs>
        <clipPath id="card-clip"><rect width="538" height="348"/></clipPath>
        <linearGradient id="house-sky" x1="0" y1="0" x2="0" y2="1">
          <stop offset="0" stop-color="#8fb6d8"/>
          <stop offset="0.45" stop-color="#d8c7a6"/>
          <stop offset="0.8" stop-color="#c9b48f"/>
          <stop offset="1" stop-color="#5f8d3d"/>
        </linearGradient>
        <linearGradient id="house-yellow" x1="0" y1="0" x2="0" y2="1">
          <stop offset="0" stop-color="#7ea9d2"/>
          <stop offset="0.3" stop-color="#d6b85a"/>
          <stop offset="0.8" stop-color="#c8a552"/>
          <stop offset="1" stop-color="#5e8c38"/>
        </linearGradient>
        <linearGradient id="house-leafy" x1="0" y1="0" x2="0" y2="1">
          <stop offset="0" stop-color="#6d9a3c"/>
          <stop offset="0.4" stop-color="#d9cdb4"/>
          <stop offset="1" stop-color="#e6e1d8"/>
        </linearGradient>
      </defs>

      <rect class="card-bg" width="538" height="348" fill="var(--forest)"/>

      <g clip-path="url(#card-clip)">
        <circle cx="432" cy="72" r="124" fill="var(--forest-ring)"/>
        <circle cx="432" cy="72" r="116" fill="url(#house-sky)" role="img" aria-label="Photo of the sold townhouse at 4127 Pembrook Street"/>

        <circle cx="98" cy="248" r="122" fill="var(--forest-ring)"/>
        <circle cx="98" cy="248" r="114" fill="url(#house-yellow)" role="img" aria-label="Photo of the sold townhouse at 4179 Pembrook Street"/>

        <circle cx="398" cy="336" r="148" fill="var(--forest-ring)"/>
        <circle cx="398" cy="336" r="140" fill="url(#house-leafy)" role="img" aria-label="Photo of the sold townhouse at 4163 Pembrook Street"/>
      </g>

      <text class="headline" x="46" y="54">Are you selling your house on</text>
      <text x="46" y="80"><tspan class="headline-area">Evergreen</tspan><tspan class="headline" dx="5">in San Jose CA?</tspan></text>
      <text class="subline" x="46" y="97">I have the highest sales in the community</text>
      <text class="back-hint" x="134" y="120">See back of the card for details →</text>

      <g class="sold-tag">
        <rect x="292" y="10" width="94" height="35" fill="var(--tag-green)"/>
        <rect x="336" y="10" width="50" height="35" fill="var(--tag-dark)"/>
        <text class="tag-street" x="297" y="22">Pembrook St</text>
        <text class="tag-number" x="297" y="39">4127</text>
        <text class="tag-sold" x="381" y="22" text-anchor="end">Sold for</text>
        <text class="tag-price" x="381" y="39" text-anchor="end">$820,488</text>
      </g>

      <g class="sold-tag">
        <rect x="433" y="213" width="91" height="35" fill="var(--tag-green)"/>
        <rect x="470" y="213" width="54" height="35" fill="var(--tag-dark)"/>
        <text class="tag-street" x="437" y="226">Pembrook St</text>
        <text class="tag-number" x="437" y="242">4163</text>
        <text class="tag-sold" x="519" y="226" text-anchor="end">Sold for</text>
        <text class="tag-price" x="519" y="242" text-anchor="end">$816,000</text>
      </g>

      <g class="sold-tag">
        <rect x="121" y="303" width="91" height="36" fill="var(--tag-green)"/>
        <rect x="158" y="303" width="54" height="36" fill="var(--tag-dark)"/>
        <text class="tag-street" x="125" y="316">Pembrook St</text>
        <text class="tag-number" x="125" y="333">4179</text>
        <text class="tag-sold" x="207" y="316" text-anchor="end">Sold for</text>
        <text class="tag-price" x="207" y="333" text-anchor="end">$810,000</text>
      </g>
    </svg>
  </section>

  <section class="card-back" aria-label="Postcard back">
    <div class="brand"><span class="brand-mark"></span>Northvale Realty</div>
    <div class="stamp-box"></div>
    <div class="address-lines"><span></span><span></span><span></span><span></span><span></span><span></span></div>

    <div class="agent-photo" role="img" aria-label="Portrait of agent Daniel Ferrante in a dark suit"></div>
    <div class="agent-panel">
      <p class="panel-title">Personalized customer service.</p>
      <p class="panel-copy">Lorem ipsum dolor sit amet, consectetur adipiscing elit, sed do eiusmod tempor incididunt ut labore et dolore magna aliqua. Ut enim ad minim veniam, quis nostrud exercitation ullamco laboris nisi ut aliquip ex ea commodo consequat.</p>
      <p class="agent-name">Daniel Ferrante</p>
      <p class="agent-licence">BRE Licence # 01938254</p>
      <p class="agent-phone">
        <svg viewBox="0 0 10 10" aria-hidden="true"><rect width="10" height="10" rx="1.5" fill="#fff"/><path d="M3 2.2l1 1.6-.6.7c.4.9 1.1 1.6 2 2l.7-.6 1.6 1-.4 1c-2.7-.3-4.6-2.2-4.9-4.9z" fill="var(--brand-red)"/></svg>
        415-555-0182
      </p>
      <p class="agent-email">daniel@northvalerealty.com</p>
    </div>
  </section>

</main>
</body>
</html>
```